Lien Post Card - (5.5 x 8.5)

FRONT OF POSTCARD
Is a Property Lien Putting Your Home at Risk?
HOA Liens • Tax Liens • Municipal Charges • Other Property-Related Liens
You may have options to resolve outstanding liens and protect your home.
A Refinance or Home Equity Line of Credit (HELOC) may help you:
✔ Pay off qualifying liens
✔ Consolidate debt into one manageable payment
✔ Access your home's equity
✔ Improve your financial flexibility
✔ Avoid additional penalties, fees, or collection actions
Don't wait until the situation becomes more difficult.
Call today for a confidential review of your options.
Bluecove Lending Group, Inc.
(800) 641-2907 x 42
www.bluecovelending.com
NMLS #738150
BACK OF POSTCARD
Your Home Equity Could Be the Solution
If you have received notices regarding:
• Delinquent Property Taxes
• HOA or Condo Association Assessments
• Municipal Utility Liens
• Special Assessments
• Other Property-Related Obligations
You may qualify for financing options designed to help satisfy those obligations and bring your property current.
Our experienced mortgage professionals can review your situation and discuss available programs, including:
• Cash-Out Refinancing
• Home Equity Lines of Credit (HELOCs)
• Home Equity Loans
• Debt Consolidation Solutions
Free Consultation • No Obligation
Contact Marcus Whitfield today at (800) 641-2907 x42 or mwhitfield@bluecovelending.com (NMLS #84617)

```html
<!DOCTYPE html>
<html lang="en">
<head>
<meta charset="utf-8">
<title>Lien Postcard – Front and Back</title>
<link rel="stylesheet" href="https://fonts.googleapis.com/css2?family=Titillium+Web:wght@400;600;700;900&display=swap">
<style>
  :root {
    --navy: #0f1d2b;
    --navy-deep: #0a1520;
    --gold: #d39a2c;
    --gold-light: #f0b43c;
    --white: #ffffff;
    --ink: #14202c;
    --line: #c9c9c9;
    --backdrop: #b7b7b7;
    --photo-top: #4a4038;
    --photo-mid: #7e5428;
    --photo-low: #2a2119;
  }
  * { margin: 0; padding: 0; box-sizing: border-box; }
  html, body { width: 1200px; height: 904px; overflow: hidden; }
  body {
    background: var(--backdrop);
    font-family: "Titillium Web", sans-serif;
    position: relative;
  }
  .postcard {
    position: absolute;
    left: 270px;
    width: 660px;
    height: 427px;
    overflow: hidden;
    box-shadow: 0 3px 10px rgba(0,0,0,.25);
  }
  .postcard--front { top: 17px; }
  .postcard--back { top: 460px; background: var(--white); }

  /* ---------- Front ---------- */
  .front-photo {
    position: absolute; inset: 0;
    background: linear-gradient(180deg, var(--photo-top) 0%, var(--photo-mid) 50%, var(--photo-low) 100%);
  }
  .front-headline {
    position: absolute; left: 34px; top: 26px;
    color: var(--white);
    font-weight: 900; font-size: 33px; line-height: 37px;
    letter-spacing: -0.3px;
    text-shadow: 0 0 2px #000, 2px 2px 3px #000;
  }
  .lien-types {
    position: absolute; left: 34px; top: 114px;
    list-style: none;
    color: var(--white);
    font-weight: 600; font-size: 20px; line-height: 23.5px;
    text-shadow: 1px 1px 2px #000;
  }
  .lien-types li { display: flex; align-items: center; gap: 6px; }
  .lien-types li span + svg { margin-left: 28px; }
  .lien-types svg { flex: none; }
  .front-promise {
    position: absolute; left: 34px; top: 189px;
    color: var(--gold-light);
    font-weight: 700; font-size: 17.5px; line-height: 20.5px;
    text-shadow: 1px 1px 2px #000;
  }
  .heloc-intro {
    position: absolute; left: 34px; top: 240px;
    color: var(--white); font-weight: 700; font-size: 11px;
    text-shadow: 1px 1px 1px #000;
  }
  .heloc-benefits {
    position: absolute; left: 34px; top: 256px;
    list-style: none;
    color: var(--white); font-size: 10px; line-height: 15.2px;
    text-shadow: 1px 1px 1px #000;
  }
  .heloc-benefits li, .tick-list li { display: flex; align-items: center; gap: 4px; }
  .urgency-band {
    position: absolute; left: 0; top: 343px; width: 441px; height: 25px;
    background: var(--gold);
    color: var(--navy); font-weight: 700; font-size: 14px;
    padding-left: 34px; line-height: 25px;
  }
  .contact-band {
    position: absolute; left: 0; top: 368px; width: 660px; height: 59px;
    background: var(--navy);
  }
  .contact-band .cta {
    position: absolute; left: 34px; top: 4px;
    color: var(--white); font-weight: 700; font-size: 11.5px;
  }
  .contact-band .company {
    position: absolute; left: 34px; top: 20px;
    color: var(--gold-light); font-weight: 700; font-size: 9.5px;
  }
  .contact-band .details {
    position: absolute; left: 34px; top: 35px;
    color: var(--white); font-size: 10px;
    display: flex; align-items: center; gap: 4px;
  }
  .contact-band .details .gap { width: 12px; }
  .nmls-badge {
    position: absolute; left: 300px; top: 28px; width: 90px; height: 20px;
    background: var(--gold); border-radius: 2px;
    color: var(--navy); font-weight: 700; font-size: 9.5px;
    text-align: center; line-height: 20px;
  }
  .brand-seal {
    position: absolute; left: 435px; top: 292px; width: 188px; height: 188px;
    border-radius: 50%; background: var(--navy-deep);
  }
  .brand-name {
    position: absolute; left: 435px; top: 332px; width: 188px;
    text-align: center;
    color: var(--gold-light); font-weight: 700; font-size: 15px; line-height: 17px;
  }

  /* ---------- Back ---------- */
  .message-side {
    position: absolute; left: 0; top: 0; width: 364px; height: 427px;
    background: var(--gold);
  }
  .back-title {
    position: absolute; left: 34px; top: 14px;
    color: var(--navy); font-weight: 900; font-size: 20px; line-height: 25px;
  }
  .info-box {
    position: absolute; left: 0; width: 358px; background: var(--white);
    padding-left: 33px; color: var(--ink);
  }
  .info-box--notices { top: 77px; height: 116px; padding-top: 6px; }
  .info-box--programs { top: 236px; height: 116px; padding-top: 5px; }
  .info-box h3 { font-weight: 700; font-size: 14px; line-height: 17px; }
  .info-box--programs h3 { font-size: 12px; line-height: 15px; }
  .tick-list { list-style: none; font-size: 11.5px; line-height: 16.9px; font-weight: 600; }
  .info-box--notices .tick-list { margin-top: 1px; }
  .info-box--programs .tick-list { margin-top: 2px; line-height: 17.3px; }
  .qualify-band {
    position: absolute; left: 0; top: 193px; width: 364px; height: 43px;
    background: var(--navy);
    color: var(--gold-light); font-weight: 700; font-size: 11.5px; line-height: 15px;
    padding: 6px 0 0 34px;
  }
  .consult-band {
    position: absolute; left: 0; top: 352px; width: 364px; height: 25px;
    color: var(--navy); font-weight: 900; font-size: 14px; line-height: 25px;
    padding-left: 34px;
  }
  .agent-band {
    position: absolute; left: 0; top: 377px; width: 364px; height: 50px;
    background: var(--navy);
    color: var(--white); font-weight: 700; font-size: 11.5px; line-height: 15px;
    padding: 5px 0 0 34px;
  }
  .agent-band p { display: flex; align-items: center; gap: 4px; }
  .agent-band .nmls { color: var(--gold-light); font-weight: 400; font-size: 9px; margin-left: 6px; }
  .address-side .mini-brand {
    position: absolute; left: 399px; top: 50px; width: 114px;
    text-align: center; color: var(--navy); font-weight: 700; font-size: 11px; line-height: 13px;
  }
  .stamp-box {
    position: absolute; left: 547px; top: 38px; width: 74px; height: 70px;
    border: 1px solid var(--line);
  }
  .address-line {
    position: absolute; left: 398px; width: 223px; height: 0;
    border-top: 1px solid var(--line);
  }
</style>
</head>
<body>

<svg width="0" height="0" style="position:absolute">
  <defs>
    <symbol id="check-box" viewBox="0 0 16 16">
      <rect x="1" y="2" width="12" height="12" rx="1.5" fill="none" stroke="#f0b43c" stroke-width="1.8"/>
      <path d="M4 8l3 3 8-9" fill="none" stroke="#f0b43c" stroke-width="2.2" stroke-linecap="round"/>
    </symbol>
    <symbol id="tick-dot" viewBox="0 0 10 10">
      <circle cx="5" cy="5" r="5" fill="#d39a2c"/>
      <path d="M2.8 5.2l1.5 1.5 3-3" fill="none" stroke="#fff" stroke-width="1.3"/>
    </symbol>
    <symbol id="phone-icon" viewBox="0 0 12 12">
      <circle cx="6" cy="6" r="6" fill="#d39a2c"/>
      <path d="M4 3.2c.4-.3.8-.2 1 .2l.4.9c.1.3 0 .5-.2.7l-.3.3c.3.7.9 1.3 1.6 1.6l.3-.3c.2-.2.4-.3.7-.2l.9.4c.4.2.5.6.2 1l-.4.5c-.4.4-1 .4-1.6.2C5.3 7.9 4.1 6.7 3.5 5.4c-.2-.6-.2-1.2.2-1.6z" fill="#0f1d2b"/>
    </symbol>
    <symbol id="globe-icon" viewBox="0 0 12 12">
      <circle cx="6" cy="6" r="5.3" fill="none" stroke="#d39a2c" stroke-width="1.2"/>
      <ellipse cx="6" cy="6" rx="2.3" ry="5.3" fill="none" stroke="#d39a2c" stroke-width="1"/>
      <path d="M.8 6h10.4M1.8 3.3h8.4M1.8 8.7h8.4" stroke="#d39a2c" stroke-width="1"/>
    </symbol>
    <symbol id="mail-icon" viewBox="0 0 12 12">
      <circle cx="6" cy="6" r="6" fill="#d39a2c"/>
      <rect x="3" y="4" width="6" height="4.2" fill="#0f1d2b"/>
      <path d="M3 4l3 2.4L9 4" fill="none" stroke="#d39a2c" stroke-width=".8"/>
    </symbol>
  </defs>
</svg>

<!-- Front of postcard -->
<section class="postcard postcard--front" aria-label="Postcard front">
  <div class="front-photo" role="img" aria-label="Photo of a city skyline at sunset reflected on a river"></div>

  <h1 class="front-headline">IS A PROPERTY LIEN PUTTING<br>YOUR HOME AT RISK?</h1>

  <ul class="lien-types">
    <li><svg width="17" height="17"><use href="#check-box"/></svg><span>HOA Liens</span><svg width="17" height="17"><use href="#check-box"/></svg><span>Tax Liens</span></li>
    <li><svg width="17" height="17"><use href="#check-box"/></svg><span>Municipal Charges</span></li>
    <li><svg width="17" height="17"><use href="#check-box"/></svg><span>Other Property-Related Liens</span></li>
  </ul>

  <p class="front-promise">You may have options to resolve<br>outstanding liens and protect your home.</p>

  <p class="heloc-intro">A Refinance or Home Equity Line of Credit (HELOC) may help you:</p>
  <ul class="heloc-benefits">
    <li><svg width="8" height="8"><use href="#tick-dot"/></svg>Pay off qualifying liens</li>
    <li><svg width="8" height="8"><use href="#tick-dot"/></svg>Consolidate debt into one manageable payment</li>
    <li><svg width="8" height="8"><use href="#tick-dot"/></svg>Access your home’s equity</li>
    <li><svg width="8" height="8"><use href="#tick-dot"/></svg>Improve your financial flexibility</li>
    <li><svg width="8" height="8"><use href="#tick-dot"/></svg>Avoid additional penalties, fees, or collection actions</li>
  </ul>

  <div class="urgency-band">Don’t wait until the situation becomes more difficult.</div>

  <div class="contact-band">
    <p class="cta">CALL TODAY FOR A CONFIDENTIAL REVIEW OF YOUR OPTIONS.</p>
    <p class="company">Bluecove Lending Group, Inc.</p>
    <p class="details">
      <svg width="11" height="11"><use href="#phone-icon"/></svg>(800) 641-2907 x 42
      <span class="gap"></span>
      <svg width="11" height="11"><use href="#globe-icon"/></svg>www.bluecovelending.com
    </p>
    <div class="nmls-badge">NMLS #738150</div>
  </div>

  <div class="brand-seal"></div>
  <p class="brand-name">BLUECOVE<br>LENDING GROUP</p>
</section>

<!-- Back of postcard -->
<section class="postcard postcard--back" aria-label="Postcard back">
  <div class="message-side">
    <h2 class="back-title">YOUR HOME EQUITY COULD BE<br>THE SOLUTION</h2>

    <div class="info-box info-box--notices">
      <h3>If you have received notices regarding:</h3>
      <ul class="tick-list">
        <li><svg width="8" height="8"><use href="#tick-dot"/></svg>Delinquent Property Taxes</li>
        <li><svg width="8" height="8"><use href="#tick-dot"/></svg>HOA or Condo Association Assessments</li>
        <li><svg width="8" height="8"><use href="#tick-dot"/></svg>Municipal Utility Liens</li>
        <li><svg width="8" height="8"><use href="#tick-dot"/></svg>Special Assessments</li>
        <li><svg width="8" height="8"><use href="#tick-dot"/></svg>Other Property-Related Obligations</li>
      </ul>
    </div>

    <p class="qualify-band">You may qualify for financing options designed to help<br>satisfy those obligations and bring your property current.</p>

    <div class="info-box info-box--programs">
      <h3>Our experienced mortgage professionals can review<br>your situation &amp; discuss available programs, including:</h3>
      <ul class="tick-list">
        <li><svg width="8" height="8"><use href="#tick-dot"/></svg>Cash-Out Refinancing</li>
        <li><svg width="8" height="8"><use href="#tick-dot"/></svg>Home Equity Lines of Credit (HELOCs)</li>
        <li><svg width="8" height="8"><use href="#tick-dot"/></svg>Home Equity Loans</li>
        <li><svg width="8" height="8"><use href="#tick-dot"/></svg>Debt Consolidation Solutions</li>
      </ul>
    </div>

    <p class="consult-band">FREE CONSULTATION • NO OBLIGATION</p>

    <div class="agent-band">
      <p>Contact Marcus Whitfield today at <svg width="10" height="10"><use href="#phone-icon"/></svg>(800) 641-2907 x42</p>
      <p>or <svg width="10" height="10"><use href="#mail-icon"/></svg>mwhitfield@bluecovelending.com<span class="nmls">(NMLS #84617)</span></p>
    </div>
  </div>

  <div class="address-side">
    <p class="mini-brand">BLUECOVE<br>LENDING GROUP</p>
    <div class="stamp-box"></div>
    <div class="address-line" style="top:212px"></div>
    <div class="address-line" style="top:259px"></div>
    <div class="address-line" style="top:304px"></div>
  </div>
</section>

</body>
</html>
```